Pay-Per-Use Production Space Warehouse/Factory/Production Space

Please refer to project requirements as attached/included. This is an introductory marketing Info graphic to capture attention or create awareness to a new, epic and unique business value preposition and business model for customer to easily launch new products/services and robust supply chain. This is a win win revolutionary business solution compare with traditional or conventional methods of outsourcing or DIY design, build, finance, operate and maintain. PROJECT Requirement to info graphic designer
1) Subject to confidentiality and all rights reserved
2) Below are some photos which you may consider to use for this work
3) Clarify and verify with us if there are any questions related to this work and design

Target Market(s)

Global, (Life sciences, food, others)

Industry/Entity Type

Medical And Science

Requirements
Must have
• Dynamic background template.
Should not have
• Monotonous and un-creative designs

```html
<!DOCTYPE html>
<html lang="en">
<head>
<meta charset="utf-8">
<title>What is Pay-Per-Use Production Space</title>
<link href="https://fonts.googleapis.com/css2?family=Montserrat:wght@300;400;500;800;900&display=swap" rel="stylesheet">
<style>
  :root {
    --orange: #e35428;
    --orange-deep: #8a2a0e;
    --slate: #58595b;
    --white: #ffffff;
    --ink: #111111;
  }
  * { margin: 0; padding: 0; box-sizing: border-box; }
  html, body { width: 848px; height: 1200px; overflow: hidden; background: var(--white); }
  body { font-family: "Montserrat", sans-serif; position: relative; }

  .hero {
    position: absolute; left: 77px; top: 77px; width: 695px; height: 684px;
    background: var(--orange); overflow: hidden;
  }
  .hero-mark { position: absolute; left: 0; top: 0; }
  .headline { position: absolute; left: 34px; top: 225px; color: var(--white); }
  .headline-intro { font-weight: 300; font-size: 66px; line-height: 66px; letter-spacing: 1px; }
  .headline-key { font-weight: 900; font-size: 64px; line-height: 66px; letter-spacing: -1px; }
  .headline-sub { font-weight: 300; font-size: 62px; line-height: 66px; letter-spacing: 1px; }

  .slogan {
    position: absolute; left: 0; width: 100%; top: 504px;
    text-align: center; font-size: 24px; line-height: 30.5px;
  }
  .slogan .strong { font-weight: 900; }
  .slogan .slate { color: var(--slate); }
  .slogan .light { font-weight: 300; color: var(--white); }
  .slogan .dark { font-weight: 400; color: var(--ink); }
  .slogan .tag-slate { background: var(--slate); color: var(--white); font-weight: 900; padding: 0 5px; }
  .slogan .tag-white { background: var(--white); color: var(--ink); font-weight: 900; padding: 0 5px; }
  .slogan .medium { font-weight: 500; }

  .how-title {
    position: absolute; left: 0; width: 848px; top: 800px; text-align: center;
    color: var(--orange); font-weight: 500; font-size: 34px; letter-spacing: 1px;
  }
  .pillar { position: absolute; top: 877px; width: 190px; text-align: center; }
  .pillar-badge {
    width: 86px; height: 86px; border-radius: 50%; margin: 0 auto;
    background: radial-gradient(circle at 30% 28%, var(--orange) 45%, var(--orange-deep) 100%);
    display: flex; align-items: center; justify-content: center;
  }
  .pillar-label {
    margin-top: 0; position: absolute; left: 0; width: 100%;
    color: var(--slate); font-weight: 500; font-size: 14px; line-height: 17px;
  }
  .divider { position: absolute; top: 981px; width: 1px; height: 60px; background: var(--slate); }
  .footnote {
    position: absolute; left: 0; width: 904px; top: 1110px; text-align: center;
    color: var(--slate); font-size: 12.5px;
  }
</style>
</head>
<body>
  <section class="hero">
    <svg class="hero-mark" width="695" height="684" viewBox="0 0 695 684" aria-hidden="true">
      <path d="M560 63 C 590 25, 660 10, 688 60 C 712 105, 690 160, 640 195 C 590 230, 570 270, 625 318"
            fill="none" stroke="var(--slate)" stroke-width="56"/>
      <circle cx="607" cy="369" r="34" fill="var(--slate)"/>
    </svg>
    <h1 class="headline">
      <div class="headline-intro">What is</div>
      <div class="headline-key">PAY-PER-USE</div>
      <div class="headline-sub">Production Space</div>
    </h1>
    <div class="slogan">
      <div><span class="strong slate">YOU USE IT, YOU PAY IT**</span></div>
      <div><span class="light">YOU DON’T USE </span><span class="medium slate">THE PRODUCTION SPACE,</span></div>
      <div><span class="tag-slate">YOU DON’T PAY</span> <span class="medium slate">FOR IT!</span></div>
      <div><span class="dark">PARTIAL USE, </span><span class="tag-white">PARTIAL PAY</span></div>
    </div>
  </section>

  <h2 class="how-title">How can these work ?</h2>

  <div class="pillar" style="left:122px">
    <div class="pillar-badge">
      <svg width="54" height="54" viewBox="0 0 54 54" fill="none" stroke="#fff" stroke-width="1.8" stroke-linecap="round" aria-hidden="true">
        <path d="M27 14 a11 11 0 0 0 -6 20 v5 h12 v-5 a11 11 0 0 0 -6 -20z"/>
        <path d="M22 42 h10 M23 45 h8"/>
        <circle cx="29" cy="24" r="3"/>
        <path d="M27 3 v5 M12 10 l3 4 M42 10 l-3 4 M6 22 h5 M43 22 h5 M10 36 l4 -3 M44 36 l-4 -3"/>
      </svg>
    </div>
    <p class="pillar-label" style="top:108px">Through Our Patented<br>&amp; Innovative Factory<br>Space Design</p>
  </div>

  <div class="divider" style="left:324px"></div>

  <div class="pillar" style="left:329px">
    <div class="pillar-badge">
      <svg width="50" height="54" viewBox="0 0 50 54" fill="none" stroke="#fff" stroke-width="1.8" stroke-linecap="round" aria-hidden="true">
        <path d="M12 14 a15 15 0 0 1 26 0"/>
        <path d="M9 24 a16 16 0 0 1 32 0 v8"/>
        <path d="M14 40 v-16 a11 11 0 0 1 22 0 v12"/>
        <path d="M19 44 v-20 a6 6 0 0 1 12 0 v14"/>
        <path d="M25 48 v-24"/>
        <path d="M9 32 v4 M36 42 l-4 4"/>
      </svg>
    </div>
    <p class="pillar-label" style="top:116px">Unique<br>Business Model</p>
  </div>

  <div class="divider" style="left:524px"></div>

  <div class="pillar" style="left:536px">
    <div class="pillar-badge">
      <svg width="50" height="54" viewBox="0 0 50 54" fill="none" stroke="#fff" stroke-width="1.8" stroke-linejoin="round" stroke-linecap="round" aria-hidden="true">
        <path d="M8 6 h14 v4 a3 3 0 0 0 6 0 v-4 h14 v18 h-34 z"/>
        <path d="M6 30 l8 -4 l8 4 l6 -4 l8 0 l8 6"/>
        <path d="M14 34 l8 8 a3 3 0 0 0 4 0 l10 -10"/>
        <path d="M18 40 l3 3 M22 44 l3 3"/>
      </svg>
    </div>
    <p class="pillar-label" style="top:111px">Due Diligence and<br>Mutual Adoption of<br>Good Practises</p>
  </div>

  <p class="footnote">**Contact us for more details, case by case basis</p>
</body>
</html>
```